Fennick Executive Search - New Business Card Design Project

We are an executive search firm called Fennick Executive Search based in the UK. We require a custom design for a business card. We're looking to convey a professional service to executives for executive search recruitment services. In terms of colours, we like dark blues and grays (maybe even silver incorporated somewhere if we go for a foiled type of card) but we're open to your artistic flare. See our current logo in attachments. We are totally open on design so long as the design is slick and professional.
Updates

Thanks for all your contributions of various designs. I have to say the quality of work has been amazing which is going to make our job quite difficult in the coming days on making a decision. Thanks to you all that have taken the time to submit designs thus far. We'll keep on reviewing and try to narrow down our selection as soon as possible.

Target Market(s)

Executive Search

Industry/Entity Type

Recruitment

Contact Information for Business Card

Fennick Executive Search,
Exclusively Sourcing & Hiring Senior Leaders
Gordon Pellbury, Managing Director,
07823 906417
0117 486 7132
gordon@fennickexecutive.co.uk
fennickexecutive.co.uk
58 Lindmoor Court, Hatherley Road, Bristol, BS32 9QJ

Font styles to use
Sans Serif
Other font styles liked:
• Roboto (which is used in our logo)

Requirements
Must have
• Our logo (It has a subtle fade on it from #02071d at top to #333649 at bottom)
• The logo can be on one side or both sides
• Must be elegant and professional
• We have 2nd slogan CONSULT | INSPIRE | INNOVATE | DELIVER which can be incorporated into the card
Nice to have
• Use of blues and grey colours
• Compatible with similar styling to our website fennickexecutive.co.uk
Should not have
• Must not be overly brash
• Must not contain cartoon characters

```html
<!DOCTYPE html>
<html lang="en">
<head>
<meta charset="utf-8">
<title>Fennick Executive Search – Business Card</title>
<link rel="stylesheet" href="https://fonts.googleapis.com/css2?family=Open+Sans:wght@400;600&family=Roboto:wght@400;500;700&display=swap">
<style>
  :root {
    --navy: #2a2c4a;
    --pill: #4a4c6e;
    --ink: #2a2c4a;
    --text: #3a3a44;
    --muted: #6b6c78;
    --paper: #ffffff;
    --backdrop: #a9a9ab;
  }
  * { box-sizing: border-box; margin: 0; padding: 0; }
  html, body {
    width: 1200px; height: 1200px; overflow: hidden;
    background: var(--backdrop);
  }
  .canvas { position: relative; width: 1200px; height: 1200px; }
  .card {
    position: absolute; left: 160px; width: 880px; height: 530px;
    background: var(--paper);
    box-shadow: 0 4px 14px rgba(0,0,0,0.18);
    overflow: hidden;
  }
  .card--front { top: 45px; }
  .card--back { top: 625px; }

  .company-name {
    font-family: "Roboto", sans-serif; font-weight: 500; color: #fff;
    font-size: 24px; line-height: 30px; letter-spacing: 0.4px;
  }

  /* Front */
  .brand-band {
    position: absolute; left: 46px; top: 0; width: 228px; height: 370px;
    background: var(--navy);
  }
  .brand-band .company-name {
    position: absolute; left: 20px; right: 20px; bottom: 18px;
  }
  .tagline {
    position: absolute; left: 46px; top: 398px;
    font-family: "Open Sans", sans-serif; font-size: 21px; line-height: 30px; color: var(--text);
  }
  .tagline strong { font-weight: 600; color: var(--ink); }

  .person { position: absolute; left: 430px; top: 78px; }
  .person__name {
    font-family: "Roboto", sans-serif; font-weight: 700; font-size: 40px; line-height: 48px;
    color: var(--ink); letter-spacing: 0.6px;
  }
  .person__role {
    font-family: "Open Sans", sans-serif; font-size: 20px; color: var(--muted); margin-top: 2px;
  }
  .contact-rail {
    position: absolute; left: 434px; top: 210px; width: 38px; height: 238px;
    border-radius: 19px; background: var(--pill);
  }
  .contact-rail svg { position: absolute; left: 9px; width: 20px; height: 20px; }
  .contacts {
    position: absolute; left: 504px; top: 0;
    font-family: "Open Sans", sans-serif; font-size: 20px; color: var(--text); line-height: 26px;
  }
  .contacts p { position: absolute; left: 0; white-space: nowrap; }

  /* Back */
  .back-band {
    position: absolute; left: 0; top: 0; width: 100%; height: 274px; background: var(--navy);
  }
  .back-band .company-name {
    position: absolute; left: 0; right: 0; bottom: 40px; text-align: center; font-size: 30px;
  }
  .slogan {
    position: absolute; left: 0; width: 100%; top: 408px; text-align: center;
    font-family: "Roboto", sans-serif; font-size: 25px; letter-spacing: 1.5px; color: var(--text);
  }
</style>
</head>
<body>
<main class="canvas">

  <section class="card card--front" aria-label="Business card front">
    <div class="brand-band">
      <p class="company-name">Fennick Executive Search</p>
    </div>
    <p class="tagline"><strong>Exclusively Sourcing &amp;</strong><br>Hiring Senior Leaders</p>

    <div class="person">
      <h1 class="person__name">GORDON PELLBURY</h1>
      <p class="person__role">Managing Director</p>
    </div>

    <div class="contact-rail" aria-hidden="true">
      <svg viewBox="0 0 24 24" style="top:14px"><path fill="#fff" d="M6.6 10.8a15.1 15.1 0 0 0 6.6 6.6l2.2-2.2c.3-.3.7-.4 1-.2 1.1.4 2.3.6 3.6.6.6 0 1 .4 1 1V20c0 .6-.4 1-1 1C10.6 21 3 13.4 3 4c0-.6.4-1 1-1h3.5c.6 0 1 .4 1 1 0 1.3.2 2.5.6 3.6.1.3 0 .7-.2 1z"/></svg>
      <svg viewBox="0 0 24 24" style="top:74px"><path fill="#fff" d="M3 5h18v14H3z"/><path fill="none" stroke="#4a4c6e" stroke-width="1.8" d="M3 5l9 8 9-8"/></svg>
      <svg viewBox="0 0 24 24" style="top:128px"><circle cx="12" cy="12" r="9" fill="#fff"/><path fill="none" stroke="#4a4c6e" stroke-width="1.4" d="M3 12h18M12 3c3 3 3 15 0 18M12 3c-3 3-3 15 0 18"/></svg>
      <svg viewBox="0 0 24 24" style="top:202px"><path fill="#fff" d="M12 2a7 7 0 0 0-7 7c0 5 7 13 7 13s7-8 7-13a7 7 0 0 0-7-7z"/><circle cx="12" cy="9" r="2.5" fill="#4a4c6e"/></svg>
    </div>

    <div class="contacts">
      <p style="top:211px">07823 906417</p>
      <p style="top:237px">0117 486 7132</p>
      <p style="top:283px">gordon@fennickexecutive.co.uk</p>
      <p style="top:335px">fennickexecutive.co.uk</p>
      <p style="top:389px">58 Lindmoor Court, Hatherley Road,</p>
      <p style="top:415px">Bristol, BS32 9QJ</p>
    </div>
  </section>

  <section class="card card--back" aria-label="Business card back">
    <div class="back-band">
      <p class="company-name">Fennick Executive Search</p>
    </div>
    <p class="slogan">CONSULT | INSPIRE | INNOVATE | DELIVER</p>
  </section>

</main>
</body>
</html>
```